Quiet Fern Acupuncture
Quiet Fern Acupuncture -
Creative Brief
Bright & Fun-filled
Marla Pennick-Vasquez
LAc, Dipl, Ac
2730 N Ridley Avenue, Suite 410 Flagstaff, AZ, 86044 @ Haverstock Chiropractic
quietfernacupuncture@mailbox-example.com
an appointment reminder card

```html
<!DOCTYPE html>
<html lang="en">
<head>
<meta charset="utf-8">
<title>Quiet Fern Acupuncture – Stationery Set</title>
<link href="https://fonts.googleapis.com/css2?family=Open+Sans:wght@400;700&display=swap" rel="stylesheet">
<style>
  :root{
    --orange:#f39200;
    --orange-deep:#e35f0c;
    --orange-soft:#fbc56a;
    --ink:#1d1d1b;
    --paper:#ffffff;
    --backdrop:#ecebe8;
    --muted:#8a8a8a;
  }
  *{box-sizing:border-box;margin:0;padding:0}
  html,body{width:1200px;height:331px;overflow:hidden;background:var(--backdrop);font-family:"Open Sans",Arial,sans-serif;color:var(--ink)}
  .set{position:relative;width:1200px;height:331px}
  .piece{position:absolute;background:var(--paper);box-shadow:0 2px 6px rgba(0,0,0,.18);overflow:hidden}
  .brand{display:flex;align-items:center;gap:4px;font-weight:700;color:var(--orange-deep);white-space:nowrap;line-height:1.15}
  .brand-dot{border-radius:50%;background:var(--orange);flex:none}
  .fine{font-size:3.6px;line-height:1.6;color:var(--muted);white-space:nowrap}
  .swoosh{position:absolute;left:0;width:100%}
  .flourish{position:absolute;border-radius:50%;background:radial-gradient(circle,rgba(190,200,230,.35),rgba(250,200,170,.18) 60%,transparent 75%)}

  /* business card */
  .business-card{left:34px;top:67px;width:120px;height:72px;background:linear-gradient(135deg,var(--paper) 60%,var(--orange-soft) 80%,var(--orange) 100%)}
  .business-card .brand{position:absolute;left:8px;top:8px;font-size:5.5px}
  .business-card .holder{position:absolute;left:8px;top:23px;font-size:4.5px;font-weight:700}
  .business-card .fine{position:absolute;left:8px;top:31px}

  /* appointment card */
  .appointment-card{left:34px;top:151px;width:120px;height:90px}
  .appointment-card .title{font-size:5px;font-weight:700;color:var(--orange-deep);padding:6px 8px 3px}
  .appointment-card .line{display:flex;gap:4px;align-items:flex-end;padding:3px 8px;font-size:4px;color:var(--muted)}
  .appointment-card .line span{flex:1;border-bottom:.5px solid #bbb;height:5px}
  .appointment-card .note{padding:4px 8px;font-size:3.6px;color:var(--muted)}

  /* letterheads */
  .letterhead{top:24px;width:158px;height:260px}
  .letterhead.primary{left:204px}
  .letterhead.follow{left:384px}
  .letterhead .brand{position:absolute;left:10px;top:11px;font-size:5.5px}
  .letterhead .address{position:absolute;right:8px;top:12px;text-align:right;font-size:3.3px}

  /* envelopes */
  .envelope{width:182px;height:90px}
  .envelope.front{left:653px;top:96px}
  .envelope.plain{left:653px;top:196px}
  .envelope .brand{position:absolute;left:10px;top:10px;font-size:5.5px}
  .envelope .fine{position:absolute;left:10px;top:20px}

  .envelope.back-black{left:880px;top:48px;width:240px;height:72px}
  .envelope.back-black .flap{position:absolute;inset:0}
  .envelope.back-orange{left:880px;top:130px;width:240px;height:72px;background:linear-gradient(180deg,var(--orange),var(--orange-deep))}
  .envelope.back-white{left:880px;top:212px;width:240px;height:80px}
  .envelope.back-white .brand,.envelope.back-black .brand,.envelope.back-orange .brand{position:absolute;font-size:6px}
</style>
</head>
<body>
<main class="set">

  <section class="piece business-card">
    <div class="brand"><span class="brand-dot" style="width:8px;height:8px"></span>Quiet Fern Acupuncture</div>
    <p class="holder">Marla Pennick-Vasquez</p>
    <div class="fine">LAc, Dipl, Ac<br>2730 N Ridley Avenue, Suite 410<br>Flagstaff, AZ, 86044 @ Haverstock Chiropractic<br>quietfernacupuncture@mailbox-example.com</div>
  </section>

  <section class="piece appointment-card">
    <p class="title">Your next appointment</p>
    <div class="line">Date<span></span></div>
    <div class="line">Day<span></span></div>
    <div class="line">Time<span></span></div>
    <p class="note">Please call to reschedule · Phone 928 555 0143</p>
  </section>

  <section class="piece letterhead primary">
    <div class="brand"><span class="brand-dot" style="width:9px;height:9px"></span><span>Quiet Fern<br>Acupuncture</span></div>
    <div class="fine address">2730 N Ridley Avenue, Suite 410<br>Flagstaff, AZ, 86044<br>quietfernacupuncture@mailbox-example.com</div>
    <div class="flourish" role="img" aria-label="Faint pastel bird and vine decoration" style="left:30px;top:70px;width:100px;height:110px"></div>
    <svg class="swoosh" style="bottom:0;height:40px" viewBox="0 0 158 40" preserveAspectRatio="none">
      <path d="M0 22 Q60 10 158 18 L158 40 L0 40Z" fill="var(--orange)"/>
      <path d="M0 16 Q70 4 158 12" stroke="var(--ink)" stroke-width="1.2" fill="none"/>
    </svg>
  </section>

  <section class="piece letterhead follow">
    <div class="flourish" role="img" aria-label="Faint pastel bird and vine decoration" style="left:30px;top:70px;width:100px;height:110px"></div>
  </section>

  <section class="piece envelope front">
    <div class="brand"><span class="brand-dot" style="width:9px;height:9px"></span>Quiet Fern Acupuncture</div>
    <div class="fine">2730 N Ridley Avenue, Suite 410<br>Flagstaff, AZ, 86044</div>
    <div class="flourish" role="img" aria-label="Faint pastel bird and vine decoration" style="left:95px;top:10px;width:75px;height:70px"></div>
    <svg class="swoosh" style="bottom:0;height:18px" viewBox="0 0 182 18" preserveAspectRatio="none">
      <path d="M0 10 Q90 2 182 8 L182 18 L0 18Z" fill="var(--orange)"/>
      <path d="M0 7 Q90 -1 182 5" stroke="var(--ink)" stroke-width="1" fill="none"/>
    </svg>
  </section>

  <section class="piece envelope plain">
    <div class="flourish" role="img" aria-label="Faint pastel bird and vine decoration" style="left:95px;top:10px;width:75px;height:70px"></div>
    <svg class="swoosh" style="bottom:0;height:18px" viewBox="0 0 182 18" preserveAspectRatio="none">
      <path d="M0 10 Q90 2 182 8 L182 18 L0 18Z" fill="var(--orange)"/>
    </svg>
  </section>

  <section class="piece envelope back-black">
    <svg class="flap" viewBox="0 0 240 72" preserveAspectRatio="none">
      <path d="M0 0 H240 L120 50Z" fill="var(--ink)"/>
      <path d="M0 0 L120 50 L240 0" stroke="#ccc" stroke-width=".6" fill="none"/>
    </svg>
    <div class="brand" style="left:88px;top:14px;color:var(--orange)"><span class="brand-dot" style="width:8px;height:8px"></span>Quiet Fern</div>
  </section>

  <section class="piece envelope back-orange">
    <svg class="swoosh" style="top:0;height:72px" viewBox="0 0 240 72" preserveAspectRatio="none">
      <path d="M0 0 H240 L120 48Z" fill="var(--paper)"/>
      <path d="M0 0 L120 48 L240 0" stroke="var(--orange-deep)" stroke-width=".8" fill="none"/>
    </svg>
    <div class="brand" style="left:88px;top:12px"><span class="brand-dot" style="width:8px;height:8px"></span>Quiet Fern</div>
  </section>

  <section class="piece envelope back-white">
    <svg class="swoosh" style="top:0;height:80px" viewBox="0 0 240 80" preserveAspectRatio="none">
      <path d="M0 0 L120 52 L240 0" stroke="#cfcfcf" stroke-width=".8" fill="none"/>
      <path d="M0 80 L100 40 M240 80 L140 40" stroke="#e2e2e2" stroke-width=".6" fill="none"/>
    </svg>
    <div class="brand" style="left:88px;top:14px"><span class="brand-dot" style="width:8px;height:8px"></span>Quiet Fern</div>
  </section>

</main>
</body>
</html>
```